Voyage Wellness Point Business Cards

We need business cards for our new start-up online travel health clinic. Visit our website voyagewellpoint.ca for branding and more info.

Target Market(s)

Travellers

Industry/Entity Type

Business

Contact Information for Business Card

Mara Kowalczyk
mara@voyagewellpoint.ca
+1 555 283 0461
voyagewellpoint.ca

Font styles to use
Sans Serif

Colors
f68d4d

```html
<!DOCTYPE html>
<html lang="en">
<head>
<meta charset="utf-8">
<title>Voyage Wellness Point Business Cards</title>
<link rel="stylesheet" href="https://fonts.googleapis.com/css2?family=Open+Sans:wght@400;600&display=swap">
<style>
  :root {
    --orange: #f68d4d;
    --grey: #8a8a8a;
    --grey-dark: #555555;
    --paper: #ffffff;
    --ink: #1d1d1d;
    --backdrop: #dedfe3;
  }
  * { box-sizing: border-box; margin: 0; padding: 0; }
  html, body {
    width: 1200px; height: 800px; overflow: hidden;
    background: var(--backdrop);
    font-family: "Open Sans", sans-serif;
  }
  .sheet {
    width: 1200px; height: 800px;
    display: flex; align-items: center; justify-content: center; gap: 40px;
  }
  .card {
    width: 520px; height: 297px; position: relative;
    box-shadow: 0 4px 14px rgba(0,0,0,0.12);
  }
  .card--front { background: var(--paper); }
  .card--back {
    background: var(--ink);
    display: flex; flex-direction: column; align-items: center; justify-content: center;
  }
  .brand {
    font-weight: 400; color: var(--orange); letter-spacing: -0.5px;
    white-space: nowrap;
  }
  .card--front .brand {
    position: absolute; left: 36px; top: 52px; font-size: 38px;
  }
  .tagline {
    color: var(--grey); font-size: 15px; font-style: italic;
  }
  .card--front .tagline {
    position: absolute; right: 42px; top: 106px;
  }
  .card--back .brand { font-size: 40px; }
  .card--back .tagline { color: #b5b5b5; margin-top: 6px; align-self: flex-end; margin-right: 60px; }
  .contact {
    position: absolute; left: 36px; bottom: 44px;
    display: flex; align-items: stretch;
  }
  .person { padding-right: 18px; text-align: right; padding-top: 4px; }
  .person__name { font-size: 17px; color: var(--grey-dark); }
  .person__first { color: var(--orange); }
  .person__role { font-size: 10.5px; color: var(--grey); margin-top: 2px; }
  .divider { width: 1px; background: #bdbdbd; }
  .details { list-style: none; padding-left: 14px; }
  .details li {
    display: flex; align-items: center; gap: 9px;
    font-size: 13px; color: var(--grey-dark); line-height: 1; margin: 4px 0;
  }
  .icon { width: 17px; height: 17px; flex: none; }
</style>
</head>
<body>
<main class="sheet">
  <section class="card card--front" aria-label="Business card front">
    <div class="brand">Voyage Wellness Point</div>
    <div class="tagline">Online Travel Health Experts</div>
    <div class="contact">
      <div class="person">
        <div class="person__name"><span class="person__first">Mara</span> Kowalczyk</div>
        <div class="person__role">Managing Director</div>
      </div>
      <div class="divider"></div>
      <ul class="details">
        <li>
          <svg class="icon" viewBox="0 0 20 20" aria-hidden="true">
            <circle cx="10" cy="10" r="9" fill="none" stroke="#f68d4d" stroke-width="1.6"/>
            <path d="M7 5.5c-1 .8-1.3 2-.6 3.5 1 2 2.5 3.6 4.5 4.6 1.4.7 2.6.4 3.4-.6l-1.6-1.6-1.3.7c-1-.5-2-1.5-2.5-2.5l.7-1.3z" fill="#f68d4d"/>
          </svg>
          +1 555 283 0461
        </li>
        <li>
          <svg class="icon" viewBox="0 0 20 20" aria-hidden="true">
            <circle cx="10" cy="10" r="9" fill="none" stroke="#f68d4d" stroke-width="1.6"/>
            <rect x="5" y="6.5" width="10" height="7" rx="1" fill="#f68d4d"/>
            <path d="M5.3 7l4.7 3.6L14.7 7" fill="none" stroke="#fff" stroke-width="1"/>
          </svg>
          mara@voyagewellpoint.ca
        </li>
        <li>
          <svg class="icon" viewBox="0 0 20 20" aria-hidden="true">
            <circle cx="10" cy="10" r="9" fill="none" stroke="#f68d4d" stroke-width="1.6"/>
            <circle cx="10" cy="10" r="5" fill="none" stroke="#f68d4d" stroke-width="1.2"/>
            <ellipse cx="10" cy="10" rx="2.2" ry="5" fill="none" stroke="#f68d4d" stroke-width="1"/>
            <path d="M5 10h10" stroke="#f68d4d" stroke-width="1"/>
          </svg>
          www.voyagewellpoint.ca
        </li>
      </ul>
    </div>
  </section>

  <section class="card card--back" aria-label="Business card back">
    <div class="brand">Voyage Wellness Point</div>
    <div class="tagline">Online Travel Health Experts</div>
  </section>
</main>
</body>
</html>
```